Brightpath EAP 2 x Flyer with Poster

Brightpath is an award-winning organisation providing dynamic and creative ways for children, young people, adults and families to make positive change and achieve fulfilling lives.
We are launching into a new area of business and starting to offer organisations Employee Assistance Program (EAP). To launch this service we need 2 flyers and a poster:
- 1 x flyer for employers
- 1 x flyer for employees
- 1 x poster (A3) for employees to be displayed around the office.
For the flyers we are after an a4 colour double sided flyer in either a A4 tri-fold to DL format or A4 bi-fold to A5 format. We are looking for a design that is simple and dynamic whilst keeping in line with our branding.
The winning designs will need to be hi-res and ready for print and also a lower res version suitable to email.
I have attached a number of files to provide further background, including:
• I have attached 3 x word doc of copy for each (2 x flyer / 1 x poster)
• Brand Guidelines
• Logo
• Our clinic flyer recently produced by a ArtHive designer for our clinic area of the business. These flyers do not have to be exactly the same as this one but should appear to be from the same organisation although a different service.
Generally we like our designs to be clear and simple.
Please don't hesitate to reach out with any Q's.

```html
<!DOCTYPE html>
<html lang="en">
<head>
<meta charset="utf-8">
<title>Brightpath Employee Assistance Program Flyer</title>
<link rel="stylesheet" href="https://fonts.googleapis.com/css2?family=Open+Sans:wght@400;600;700&display=swap">
<style>
  :root {
    --backdrop: #b7c9bb;
    --sage: #7fa38b;
    --sage-dark: #6e937b;
    --peach: #e3b49f;
    --charcoal: #3a3a3a;
    --photo-light: #9a9a9a;
    --photo-dark: #3c3c3c;
    --white: #ffffff;
    --text-soft: #f4f6f3;
  }
  * { box-sizing: border-box; margin: 0; padding: 0; }
  html, body {
    width: 1200px; height: 900px; overflow: hidden;
    background: var(--backdrop);
    font-family: "Open Sans", sans-serif;
  }
  .flyer {
    position: absolute; left: 294px; top: 20px;
    width: 612px; height: 860px;
    background: var(--sage);
    overflow: hidden;
    color: var(--white);
  }
  .hero-photo {
    position: absolute; left: 0; top: 0; width: 612px; height: 350px;
    background: linear-gradient(120deg, var(--photo-light) 0%, #6c6c6c 45%, var(--photo-dark) 75%, #7a7a7a 100%);
  }
  .hero-shape { position: absolute; left: 0; top: 0; }
  .title {
    position: absolute; left: 53px; top: 20px;
    font-size: 36px; font-weight: 700; line-height: 40px;
  }
  .subtitle {
    position: absolute; left: 53px; top: 114px;
    font-size: 15px; font-weight: 700;
  }
  .phone-pill {
    position: absolute; left: 70px; top: 168px;
    width: 186px; height: 23px;
    background: var(--peach); border-radius: 0 12px 12px 0;
  }
  .phone-icon { position: absolute; left: 54px; top: 166px; }
  .phone-number {
    position: absolute; left: 90px; top: 166px;
    font-size: 19px; line-height: 26px;
  }
  .contact {
    position: absolute; left: 81px; top: 197px; line-height: 1.3;
  }
  .contact .email { font-size: 18px; }
  .contact .org { font-size: 15px; margin-bottom: 2px; }
  .contact .line { font-size: 11.5px; line-height: 19px; }
  .section-head {
    position: absolute; left: 0; height: 20px;
    background: var(--peach); border-radius: 0 11px 11px 0;
    padding-left: 54px; padding-right: 12px;
    font-size: 16px; line-height: 20px;
  }
  .body-copy {
    position: absolute; left: 53px; width: 522px;
    font-size: 9.5px; line-height: 11.7px; color: var(--text-soft);
  }
  .lead { font-size: 12px; }
  .checklist { position: absolute; list-style: none; }
  .checklist li {
    font-size: 9.5px; height: 14.7px; line-height: 14.7px;
    display: flex; align-items: center; gap: 8px; color: var(--text-soft);
  }
</style>
</head>
<body>
<svg width="0" height="0" style="position:absolute">
  <defs>
    <symbol id="tick-box" viewBox="0 0 12 12">
      <rect x="1" y="2" width="8" height="8" fill="none" stroke="#e3b49f" stroke-width="1"/>
      <path d="M3 6 L5 8.5 L11 1" fill="none" stroke="#e3b49f" stroke-width="1.3"/>
    </symbol>
  </defs>
</svg>

<main class="flyer">
  <div class="hero-photo" role="img" aria-label="Black and white photo of three colleagues talking around a meeting table"></div>
  <svg class="hero-shape" width="612" height="360" viewBox="0 0 612 360" aria-hidden="true">
    <path d="M0 282 Q100 320 160 338 Q180 344 200 336 L612 168 L612 360 L0 360 Z" fill="none" stroke="#3a3a3a" stroke-width="5"/>
    <path d="M0 282 Q100 320 160 338 Q180 344 200 336 L612 168 L612 360 L0 360 Z" fill="#7fa38b"/>
  </svg>

  <h1 class="title">Employee Assistance<br>Program (EAP)</h1>
  <p class="subtitle">Counselling for Work Related or Personal Issues</p>

  <div class="phone-pill"></div>
  <svg class="phone-icon" width="27" height="27" viewBox="0 0 27 27" aria-hidden="true">
    <circle cx="13.5" cy="13.5" r="12" fill="#ffffff" stroke="#6e937b" stroke-width="2"/>
    <path d="M9.5 7.5 L11.5 7 L12.5 10 L11 11 Q12 14.5 15.5 16 L16.5 14.5 L19.5 15.5 L19 17.5 Q16 20 11.5 15.5 Q7 11 9.5 7.5 Z" fill="#6e937b"/>
  </svg>
  <p class="phone-number">03 9000 4812</p>

  <address class="contact" style="font-style:normal">
    <p class="email">clinic@brightpath.au</p>
    <p class="org">Brightpath</p>
    <p class="line">Foundry House</p>
    <p class="line">42 Riverbend Rd, Northvale VIC 3070</p>
    <p class="line">brightpath.au</p>
  </address>

  <h2 class="section-head" style="top:355px">Employee Assistance Program</h2>
  <p class="body-copy" style="top:377px">Employee Assistance Program (EAP) is a confidential employer-funded support service available to employees and immediate family members experiencing personal or work-related concerns. Immediate family include your spouse, partner, children or others living in your household.</p>

  <h2 class="section-head" style="top:420px">Counselling Services</h2>
  <p class="body-copy lead" style="top:446px">EAP is provided for a variety of personal, emotional and work-related matters including:</p>
  <ul class="checklist" style="left:70px; top:462px">
    <li><svg width="12" height="12"><use href="#tick-box"/></svg>Anxiety</li>
    <li><svg width="12" height="12"><use href="#tick-box"/></svg>Depression and emotional wellbeing</li>
    <li><svg width="12" height="12"><use href="#tick-box"/></svg>Workplace conflict or disharmony</li>
    <li><svg width="12" height="12"><use href="#tick-box"/></svg>Coping with organisational change</li>
    <li><svg width="12" height="12"><use href="#tick-box"/></svg>Stress and burnout</li>
    <li><svg width="12" height="12"><use href="#tick-box"/></svg>Bullying</li>
    <li><svg width="12" height="12"><use href="#tick-box"/></svg>Sexual harassment</li>
    <li><svg width="12" height="12"><use href="#tick-box"/></svg>Self-esteem</li>
  </ul>
  <ul class="checklist" style="left:362px; top:462px">
    <li><svg width="12" height="12"><use href="#tick-box"/></svg>Reactions to traumatic or distressing events</li>
    <li><svg width="12" height="12"><use href="#tick-box"/></svg>Critical incidents</li>
    <li><svg width="12" height="12"><use href="#tick-box"/></svg>Grief and bereavement</li>
    <li><svg width="12" height="12"><use href="#tick-box"/></svg>Substance misuse</li>
    <li><svg width="12" height="12"><use href="#tick-box"/></svg>Domestic violence</li>
    <li><svg width="12" height="12"><use href="#tick-box"/></svg>Interpersonal relationships</li>
    <li><svg width="12" height="12"><use href="#tick-box"/></svg>Schooling and study difficulties.</li>
  </ul>

  <h2 class="section-head" style="top:590px">Who Pays for the Service?</h2>
  <p class="body-copy" style="top:614px">Your employer will pay for an agreed number of sessions. You are not required to pay for using the Brightpath EAP service. The number of available sessions depends on the agreement we have with your employer.</p>

  <h2 class="section-head" style="top:645px">Is it Confidential?</h2>
  <p class="body-copy" style="top:670px">All employee personal information collated by Brightpath during the provision of counselling services will remain confidential and secure except when subpoenaed by a court or failure to disclose the information would place the employee and/or another person at risk. Confidentiality and limitations of confidentiality are explained to employees at the beginning of the counselling process.</p>

  <h2 class="section-head" style="top:724px">How do I make an EAP Appointment</h2>
  <p class="body-copy" style="top:746px">You can make a confidential appointment directly with Brightpath through our direct line on 03 9000 4812 or via clinic@brightpath.au</p>

  <h2 class="section-head" style="top:777px">About Brightpath</h2>
  <p class="body-copy" style="top:800px">Brightpath provides a confidential and effective counselling process that is solution-focused and practical. The service is aimed at enhancing wellbeing and mental health, and can be accessed via face-to-face consultations, and by Telehealth or phone. Accessing assistance is an act of independence and strength which can empower you to make positive changes in your life.</p>
</main>
</body>
</html>
```